Design Our Holiday Magic Coupon

Purpose - The purpose of this project is to create a festive, uplifting, and visually engaging physical coupon that will be mailed to our existing community and warm leads.
The intent is twofold: first, to spark delight and connection by offering a tangible, personal touch during the holiday season; and second, to encourage customers to explore and purchase our programs as they prepare for a strong start to 2026. This mailer is designed to re-engage past buyers, inspire current participants, and gently invite new momentum into their practice through a simple, friendly offer.

Project Description + Scope

This project includes the design and production of a printed coupon ( card format) featuring a 20% discount on purchases of $79 or more. The copy should feel warm, clear, and celebratory without urgency or pressure.

The front of the card will include the headline (“Live Your Best 2026”), bold discount information, and the coupon code FESTIVE20. The back will include a short message reinforcing the tone of possibility and ease, plus simple redemption instructions and the expiry date: December 31, 2025. Deliverables include print-ready artwork, color selection aligned with KH brand style.

one side
LIVE YOUR BEST 2026
Enjoy 20% OFF when you buy $79 or more.
Use code: FESTIVE20
Redeem until end of day December 31, 2025.

Back side - Move with clarity.
Heal with intelligence.
Lead with ease.
Thank you for being part of Kinetic Harmony.
Lots of love, Mara and the whole of Team Mara

Target Market(s)

yoga teachers, yoga lovers, mostly over 50 years, women

Font styles to use
Other font styles liked:
• see attached for feel

Colors
0054AA
0677BA
7BADD7
CADEEF
E8F1F8
0094D4
00A9DD
6FCCEA
C7EBF8
E9F6FB
00AB8E
00BBA5
67D7C9
C6EFE9
E9F9F6
EB3D1F
EC4F4E
F09395
F8D3D4
FCEDEE

Requirements
Nice to have
• see attached

```html
<!DOCTYPE html>
<html lang="en">
<head>
<meta charset="utf-8">
<title>Kinetic Harmony – Holiday Coupon</title>
<link rel="stylesheet" href="https://fonts.googleapis.com/css2?family=Alegreya:wght@400;500;700;800&family=Lexend:wght@400;500;600&display=swap">
<style>
  :root {
    --navy: #0f2139;
    --card-deep: #4c84bd;
    --card-mid: #6a9ccd;
    --card-light: #9cbfe0;
    --white: #ffffff;
    --soft-white: rgba(255, 255, 255, 0.16);
    --code-ink: #4a82bc;
  }
  * { box-sizing: border-box; margin: 0; padding: 0; }
  html, body { width: 791px; height: 1200px; overflow: hidden; }
  body {
    background: var(--navy);
    position: relative;
    font-family: "Alegreya", Georgia, serif;
    color: var(--white);
  }
  .card {
    position: absolute;
    left: 138px;
    width: 523px;
    height: 522px;
    overflow: hidden;
    background: linear-gradient(225deg, var(--card-light) 0%, var(--card-mid) 40%, var(--card-deep) 70%, var(--card-mid) 100%);
  }
  .card--front { top: 54px; }
  .card--back { top: 622px; }

  .abs { position: absolute; }
  .decor {
    position: absolute;
    border-radius: 50%;
    background: radial-gradient(circle, rgba(255,255,255,0.18) 0%, rgba(255,255,255,0.08) 55%, rgba(255,255,255,0) 72%);
  }
  .figure {
    position: absolute;
    border-radius: 40px;
    background: radial-gradient(ellipse, rgba(255,255,255,0.14) 0%, rgba(255,255,255,0.04) 70%, rgba(255,255,255,0) 100%);
  }
  .dot { display: inline-block; width: 12px; height: 12px; border-radius: 50%; background: var(--white); flex: none; }
  .dots { flex: none; height: 2px; background: radial-gradient(circle, var(--white) 0.9px, transparent 1.1px) 0 0 / 4px 2px repeat-x; }

  /* Front */
  .brand-mark { left: 241px; top: 56px; width: 42px; height: 42px; border-radius: 50%; background: var(--white); }
  .brand-name { left: 0; width: 100%; top: 116px; text-align: center; font-size: 25px; font-weight: 400; }
  .headline-kicker { left: 0; width: 100%; top: 186px; text-align: center; padding-left: 18px; font-weight: 700; font-size: 21px; letter-spacing: 3.4px; }
  .headline-year { left: 0; width: 100%; top: 206px; text-align: center; padding-left: 18px; font-family: "Lexend", Arial, sans-serif; font-weight: 600; font-size: 80px; line-height: 1; letter-spacing: 1px; }
  .rule-front { left: 132px; top: 291px; width: 262px; }

  .offer-enjoy { left: 70px; top: 302px; font-size: 60px; font-weight: 700; line-height: 1; letter-spacing: -1px; }
  .offer-pct { left: 70px; top: 362px; font-size: 36px; font-weight: 700; line-height: 1; }
  .offer-pct .num { font-family: "Lexend", Arial, sans-serif; font-weight: 600; font-size: 35px; }
  .offer-when { left: 263px; top: 314px; font-size: 27px; font-weight: 700; line-height: 0.97; }
  .offer-price { left: 346px; top: 302px; font-family: "Lexend", Arial, sans-serif; font-weight: 600; font-size: 64px; line-height: 1; letter-spacing: -1px; }
  .offer-price sup { font-size: 36px; vertical-align: 22px; margin-right: 2px; }
  .offer-more { left: 349px; top: 366px; font-size: 29px; font-weight: 700; line-height: 1; }

  .code-row { left: 69px; top: 415px; width: 385px; height: 32px; display: flex; align-items: center; gap: 6px; }
  .code-box { display: flex; height: 32px; border: 1.5px solid var(--white); border-radius: 3px; overflow: hidden; font-family: "Lexend", Arial, sans-serif; font-size: 17px; letter-spacing: 1.6px; }
  .code-label { width: 121px; display: flex; align-items: center; justify-content: center; }
  .code-value { width: 130px; display: flex; align-items: center; justify-content: center; background: var(--white); color: var(--code-ink); font-weight: 500; }
  .redeem { left: 0; width: 100%; top: 463px; text-align: center; font-family: "Lexend", Arial, sans-serif; font-size: 11.5px; font-weight: 500; letter-spacing: 1.4px; }

  /* Back */
  .values { left: 137px; top: 180px; list-style: none; }
  .values li { display: flex; align-items: center; gap: 16px; height: 48px; font-size: 31px; font-weight: 700; }
  .values .dot { margin-top: 4px; }
  .underlined { position: relative; }
  .underlined::after { content: ""; position: absolute; left: 0; right: 0; bottom: -1px; height: 2px; background: radial-gradient(circle, var(--white) 0.9px, transparent 1.1px) 0 0 / 4px 2px repeat-x; }
  .thanks-row { left: 67px; top: 348px; width: 386px; height: 28px; display: flex; align-items: center; gap: 7px; font-size: 21px; font-weight: 700; }
  .thanks-row .text { white-space: nowrap; }
  .sign-mark { left: 175px; top: 381px; width: 72px; height: 72px; border-radius: 50%; background: var(--white); }
  .sign-name { left: 258px; top: 387px; font-size: 20px; font-weight: 700; line-height: 1.3; }
  .signoff { left: 0; width: 100%; top: 462px; text-align: center; font-size: 14px; letter-spacing: 1.3px; }
</style>
</head>
<body>

<section class="card card--front" aria-label="Coupon front">
  <div class="decor" role="img" aria-label="Faint swirling petal pattern" style="left:-80px; top:-70px; width:240px; height:240px;"></div>
  <div class="decor" role="img" aria-label="Faint swirling petal pattern" style="left:360px; top:-50px; width:240px; height:240px;"></div>

  <span class="abs brand-mark" aria-hidden="true"></span>
  <p class="abs brand-name">Kinetic Harmony</p>

  <div class="figure" role="img" aria-label="Line drawing of a woman seated cross-legged in prayer pose" style="left:60px; top:193px; width:86px; height:100px;"></div>
  <div class="figure" role="img" aria-label="Line drawing of a woman in a standing forward fold" style="left:377px; top:193px; width:86px; height:100px;"></div>

  <p class="abs headline-kicker">LIVE YOUR BEST</p>
  <p class="abs headline-year">2026</p>
  <div class="abs dots rule-front"></div>

  <p class="abs offer-enjoy">ENJOY</p>
  <p class="abs offer-pct"><span class="num">20%</span> OFF</p>
  <p class="abs offer-when">WHEN<br>YOU<br>BUY</p>
  <p class="abs offer-price"><sup>$</sup>79</p>
  <p class="abs offer-more">or more</p>

  <div class="abs code-row">
    <span class="dot"></span>
    <span class="dots" style="width:32px"></span>
    <div class="code-box">
      <span class="code-label">USE CODE</span>
      <span class="code-value">FESTIVE20</span>
    </div>
    <span class="dots" style="width:32px"></span>
    <span class="dot"></span>
  </div>
  <p class="abs redeem">Redeem until end of day December 31, 2025</p>
</section>

<section class="card card--back" aria-label="Coupon back">
  <div class="decor" role="img" aria-label="Large faint swirling petal pattern" style="left:170px; top:-120px; width:420px; height:420px;"></div>

  <div class="figure" role="img" aria-label="Line drawing of a woman in tree pose, arms raised" style="left:39px; top:29px; width:82px; height:293px;"></div>

  <ul class="abs values">
    <li><span class="dot"></span><span>Move with <span class="underlined">clarity</span></span></li>
    <li><span class="dot"></span><span>Heal with <span class="underlined">intelligence</span></span></li>
    <li><span class="dot"></span><span>Lead with <span class="underlined">ease</span></span></li>
  </ul>

  <div class="abs thanks-row">
    <span class="dot"></span>
    <span class="dots" style="width:28px"></span>
    <span class="text">Thank you for being part of</span>
    <span class="dots" style="width:28px"></span>
    <span class="dot"></span>
  </div>

  <span class="abs sign-mark" aria-hidden="true"></span>
  <p class="abs sign-name">Kinetic<br>Harmony</p>

  <p class="abs signoff">Lots of love, Mara and the whole of Team Mara</p>
</section>

</body>
</html>
```